Boat business cards

I'm looking for business cards with the two logos I've attached. I don't have an specific idea in mind and open to anything. All the usual info will be on the card. Name, position in company, nr, email, address, ect. The company rents out these two boats for charters and fishing.

```html
<!DOCTYPE html>
<html lang="en">
<head>
<meta charset="utf-8">
<title>Charter Business Card</title>
<link href="https://fonts.googleapis.com/css2?family=Open+Sans:wght@400;600&display=swap" rel="stylesheet">
<style>
  :root {
    --backdrop: #c9cccf;
    --sky: #6f91bb;
    --brand-blue: #6e97c6;
    --wave-blue-top: #7ba2cd;
    --wave-blue-bottom: #6c8db7;
    --sand: #8b6a47;
    --ink: #1d1d1d;
    --ink-soft: #454545;
    --paper: #ffffff;
  }
  * { margin: 0; padding: 0; box-sizing: border-box; }
  html, body {
    width: 1200px; height: 928px; overflow: hidden;
    background: var(--backdrop);
    font-family: "Open Sans", sans-serif;
  }
  .canvas { position: relative; width: 1200px; height: 928px; }
  .card {
    position: absolute; border-radius: 14px; overflow: hidden;
  }
  .card-front {
    left: 267px; top: 59px; width: 670px; height: 382px;
    background: var(--sky);
  }
  .front-brand {
    position: absolute; left: 0; right: 0; top: 210px;
    text-align: center; font-weight: 600; font-size: 36px;
    color: var(--ink); letter-spacing: 1px;
  }
  .card-back {
    left: 264px; top: 484px; width: 676px; height: 387px;
    background: var(--paper);
  }
  .person-name {
    position: absolute; left: 57px; top: 43px;
    font-size: 27px; font-weight: 600; color: var(--brand-blue);
  }
  .person-role {
    position: absolute; left: 57px; top: 83px;
    font-size: 15px; color: var(--ink);
  }
  .contact-list { position: absolute; left: 56px; top: 152px; list-style: none; }
  .contact-item {
    display: flex; align-items: center; gap: 8px;
    height: 29px; font-size: 15.5px; color: var(--ink);
  }
  .contact-icon { width: 16px; height: 16px; flex: none; }
  .wave { position: absolute; left: 0; top: 0; width: 676px; height: 387px; }
  .address {
    position: absolute; left: 57px; top: 299px;
    color: var(--paper); font-size: 15.5px; line-height: 27px;
  }
  .boat-brand {
    position: absolute; left: 400px; top: 185px; width: 240px;
    text-align: center; font-weight: 600; font-size: 30px; color: var(--ink-soft);
  }
</style>
</head>
<body>
<div class="canvas">
  <section class="card card-front">
    <div class="front-brand">Silver Tide</div>
  </section>

  <section class="card card-back">
    <svg class="wave" viewBox="0 0 676 387" aria-hidden="true">
      <defs>
        <linearGradient id="seaFill" x1="0" y1="0" x2="0" y2="1">
          <stop offset="0" stop-color="var(--wave-blue-top)"/>
          <stop offset="1" stop-color="var(--wave-blue-bottom)"/>
        </linearGradient>
      </defs>
      <path d="M0,266 C120,248 250,266 380,306 C480,336 580,338 676,330 L676,387 L0,387 Z" fill="var(--sand)"/>
      <path d="M0,284 C130,268 262,292 400,334 C500,362 600,368 676,361 L676,387 L0,387 Z" fill="url(#seaFill)" stroke="#ffffff" stroke-width="3"/>
    </svg>

    <h1 class="person-name">Clara Benton</h1>
    <p class="person-role">Director</p>

    <ul class="contact-list">
      <li class="contact-item">
        <svg class="contact-icon" viewBox="0 0 16 16"><path fill="var(--sand)" d="M3.6 1.2l2.2 2.6c.3.4.3.9 0 1.3L4.7 6.3c.9 2 2.6 3.8 4.8 4.9l1.2-1.1c.4-.3.9-.4 1.3 0l2.6 2.1c.4.3.4.9.1 1.3l-1.2 1.4c-.5.5-1.2.7-1.9.5C6.3 14.1 2 9.8.7 4.5.5 3.8.7 3 1.2 2.5L2.3 1.2c.4-.4 1-.4 1.3 0z"/></svg>
        <span>555-014-2290</span>
      </li>
      <li class="contact-item">
        <svg class="contact-icon" viewBox="0 0 16 16"><rect x="0.5" y="3" width="15" height="10.5" rx="1" fill="var(--sand)"/><path d="M1.5 4l6.5 5 6.5-5" fill="none" stroke="#fff" stroke-width="1.3"/></svg>
        <span>clara@harborlinecharters.com</span>
      </li>
      <li class="contact-item">
        <svg class="contact-icon" viewBox="0 0 16 16"><circle cx="8" cy="8" r="7.5" fill="var(--sand)"/><ellipse cx="8" cy="8" rx="3" ry="7" fill="none" stroke="#fff" stroke-width="1"/><path d="M1 8h14M2.5 4.5h11M2.5 11.5h11" stroke="#fff" stroke-width="1"/></svg>
        <span>www.harborlinecharters.com</span>
      </li>
    </ul>

    <div class="boat-brand">Open Water 42</div>

    <address class="address" style="font-style:normal">
      1420 Marina Bay Rd<br>
      Port Haven, OH 45000
    </address>
  </section>
</div>
</body>
</html>
```